Olvarin Zinfandel wine label

I need a wine label designed for a new wine brand. I am open to anything, but I think the simpler and bolder the better so it will stand out on the shelf amongst the hundreds of brands out there.
Label should have the word OLVARIN buy itself with the word Zinfandel under it.

```html
<!DOCTYPE html>
<html lang="en">
<head>
<meta charset="utf-8">
<title>Olvarin Zinfandel – Wine Label</title>
<link rel="stylesheet" href="https://fonts.googleapis.com/css2?family=Cousine&family=Noto+Sans:wght@600&display=swap">
<style>
  :root {
    --label-magenta: #d60fd6;
    --oval-black: #050505;
  }
  html, body {
    margin: 0;
    padding: 0;
    width: 1200px;
    height: 720px;
    overflow: hidden;
    background: var(--label-magenta);
  }
  .wine-label {
    position: relative;
    width: 1200px;
    height: 720px;
    background: var(--label-magenta);
    overflow: hidden;
  }
  .label-oval {
    position: absolute;
    inset: 0;
    width: 1200px;
    height: 720px;
  }
  .label-oval ellipse {
    fill: var(--oval-black);
  }
  .brand-name {
    position: absolute;
    left: 0;
    width: 1200px;
    top: 276px;
    margin: 0;
    text-align: center;
    font-family: "Cousine", "Liberation Mono", "DejaVu Sans Mono", monospace;
    font-weight: 400;
    font-size: 166px;
    line-height: 180px;
    letter-spacing: 0;
    color: var(--label-magenta);
  }
  .varietal {
    position: absolute;
    left: 1065px;
    top: 360px;
    margin: 0;
    transform: translate(-50%, -50%) rotate(90deg);
    font-family: "Noto Sans", sans-serif;
    font-weight: 600;
    font-size: 34px;
    line-height: 1;
    color: var(--label-magenta);
    white-space: nowrap;
  }
</style>
</head>
<body>
  <main class="wine-label">
    <svg class="label-oval" viewBox="0 0 1200 720" aria-hidden="true">
      <ellipse cx="600" cy="360" rx="804" ry="223"/>
    </svg>
    <h1 class="brand-name">OLVARIN</h1>
    <p class="varietal">Zinfandel</p>
  </main>
</body>
</html>
```